New Business Cards for MB&LR

We need updated business cards for a staff of 15 engineers, estimators, project managers, and sales people. We have recently begun changes to our website and marketing material to improve our look and branding. We are an established fabricator specializing in pressure vessels, tanks, and structural steel. The owners require us to use the existing logo and old english text design. Also, we prefer dark grey or mostly black cards.
Target Market(s)
Engineers, purchasing agents, estimators, and project managers of; mining companies, refineries, industrial construction professionals
Industry/Entity Type
Business
Contact Information for Business Card
Logo, phone, website, email, etc.
Look and feel

```html
<!DOCTYPE html>
<html lang="en">
<head>
<meta charset="utf-8">
<title>MB&amp;LR Business Card</title>
<link rel="stylesheet" href="https://fonts.googleapis.com/css2?family=Open+Sans:wght@400;600&display=swap">
<style>
  :root {
    --backdrop: #2b2b2b;
    --card: #070707;
    --silver: #d4d4d4;
    --silver-dim: #a9a9a9;
    --text: #c9c9c9;
    --text-strong: #f2f2f2;
    --rule: #3a3a3a;
  }
  html, body {
    margin: 0;
    padding: 0;
    width: 1200px;
    height: 716px;
    overflow: hidden;
    background: var(--backdrop);
    font-family: "Open Sans", Arial, sans-serif;
  }
  .canvas {
    position: relative;
    width: 1200px;
    height: 716px;
  }
  .card {
    position: absolute;
    top: 210px;
    width: 520px;
    height: 297px;
    background: var(--card);
    box-shadow: 0 8px 24px rgba(0,0,0,.45);
  }
  .card-front { left: 50px; }
  .card-back { left: 630px; }

  .brand {
    display: flex;
    align-items: center;
    gap: 10px;
    color: var(--silver);
    font-weight: 600;
  }
  .brand-dot {
    width: 14px;
    height: 14px;
    border-radius: 50%;
    background: var(--silver);
  }
  .card-front .brand {
    position: absolute;
    left: 44px;
    top: 128px;
    font-size: 34px;
    letter-spacing: 1px;
  }
  .divider {
    position: absolute;
    left: 262px;
    top: 60px;
    width: 1px;
    height: 178px;
    background: var(--rule);
  }
  .details {
    position: absolute;
    left: 284px;
    top: 62px;
    color: var(--text);
    font-size: 11.5px;
    line-height: 17px;
  }
  .person-name {
    color: var(--text-strong);
    font-weight: 600;
    font-size: 15px;
    line-height: 19px;
  }
  .person-role { margin-bottom: 12px; }
  .address { margin-bottom: 12px; }
  .contact-list { list-style: none; margin: 0; padding: 0; }
  .contact-list li { display: flex; align-items: center; gap: 8px; }
  .contact-list svg { width: 10px; height: 10px; fill: none; stroke: var(--text); stroke-width: 1.6; }

  .card-back .brand {
    position: absolute;
    left: 0;
    right: 0;
    top: 88px;
    justify-content: center;
    font-size: 38px;
    letter-spacing: 1px;
  }
  .company-name {
    position: absolute;
    left: 0;
    right: 0;
    top: 170px;
    text-align: center;
    color: var(--silver-dim);
    font-size: 20px;
    letter-spacing: .5px;
  }
</style>
</head>
<body>
<main class="canvas">
  <section class="card card-front">
    <div class="brand"><span class="brand-dot"></span>MB&amp;LR</div>
    <div class="divider"></div>
    <div class="details">
      <div class="person-name">Evan Carter</div>
      <div class="person-role">President</div>
      <div class="address">48 Ridge Mill Road<br>Granite Falls, ID 83401</div>
      <ul class="contact-list">
        <li><svg viewBox="0 0 10 10"><path d="M2 1 L4 3 L3 4.5 Q4.5 6.5 5.5 7 L7 6 L9 8 L7.5 9.5 Q3 9 0.5 2.5 Z"/></svg>555.310.4472</li>
        <li><svg viewBox="0 0 10 10"><rect x="1" y="4" width="8" height="4"/><rect x="2.5" y="1" width="5" height="3"/><rect x="2.5" y="7" width="5" height="2"/></svg>555.310.4473</li>
        <li><svg viewBox="0 0 10 10"><rect x="1" y="2" width="8" height="6"/><path d="M1 2 L5 5.5 L9 2"/></svg>evan@mbandlr.com</li>
        <li><svg viewBox="0 0 10 10"><circle cx="5" cy="5" r="4"/><ellipse cx="5" cy="5" rx="1.8" ry="4"/><path d="M1 5 H9"/></svg>www.mbandlr.com</li>
      </ul>
    </div>
  </section>

  <section class="card card-back">
    <div class="brand"><span class="brand-dot"></span>MB&amp;LR</div>
    <div class="company-name">Mesa Beam &amp; Lintel Rolling</div>
  </section>
</main>
</body>
</html>
```